Nightclub promoter business cards

We need business cards designed for our company based in Toronto, Canada called "NowQuillo". We are an events company that promotes weekly parties in the city. We cater to a 25+ crowd and feel like our brand should reflect that. We are looking for business cards that are textured and contain a unique design. We would prefer black cards. The final design should communicate the finest hospitality and prestige. I've attached files containing our logo. For more info. about our brand visit our website at www.nowquillo-example.com.

Industry/Entity Type

Business

```html
<!DOCTYPE html>
<html lang="en">
<head>
<meta charset="utf-8">
<title>NowQuillo Business Cards</title>
<link rel="stylesheet" href="https://fonts.googleapis.com/css2?family=Cabin:wght@400;500&display=swap">
<style>
  :root {
    --page-bg: #ffffff;
    --card-black: #000000;
    --quilt-dark: #111111;
    --quilt-mid: #232323;
    --band-top: #2c2c2c;
    --band-mid: #3e3e3e;
    --band-bottom: #1e1e1e;
    --gold: #c9962a;
    --gold-light: #e3b64a;
  }
  * { margin: 0; padding: 0; box-sizing: border-box; }
  html, body {
    width: 1200px;
    height: 927px;
    overflow: hidden;
    background: var(--page-bg);
    font-family: "Cabin", "Gill Sans", sans-serif;
  }
  .canvas {
    position: relative;
    width: 1200px;
    height: 927px;
  }

  /* Front card */
  .card-front {
    position: absolute;
    left: 138px;
    top: 112px;
    width: 632px;
    height: 362px;
    background: var(--card-black);
    border: 4px solid var(--card-black);
    overflow: hidden;
  }
  .quilt-area {
    position: absolute;
    left: 0;
    width: 100%;
    background: radial-gradient(ellipse at center, var(--quilt-mid) 0%, var(--quilt-dark) 80%);
  }
  .quilt-area--top { top: 0; height: 124px; }
  .quilt-area--bottom { bottom: 0; height: 117px; }
  .name-band {
    position: absolute;
    left: 0;
    top: 124px;
    width: 100%;
    height: 117px;
    background: linear-gradient(to bottom, var(--band-top) 0%, var(--band-mid) 45%, var(--band-bottom) 100%);
    box-shadow: 0 0 8px rgba(0,0,0,.8);
    display: flex;
    align-items: center;
  }
  .brand-name {
    color: var(--gold);
    font-weight: 500;
    letter-spacing: 1px;
    line-height: 1;
  }
  .name-band .brand-name {
    margin-left: 160px;
    font-size: 66px;
  }

  /* Back card */
  .card-back {
    position: absolute;
    left: 454px;
    top: 507px;
    width: 632px;
    height: 360px;
    background: var(--card-black);
  }
  .brand-name--vertical {
    position: absolute;
    left: 80px;
    top: 195px;
    font-size: 54px;
    transform: translate(-50%, -50%) rotate(-90deg);
    white-space: nowrap;
  }
  .divider {
    position: absolute;
    left: 154px;
    top: 46px;
    width: 2px;
    height: 272px;
  }
  .contact {
    position: absolute;
    left: 203px;
    top: 129px;
    list-style: none;
    color: var(--gold-light);
    font-size: 27px;
    line-height: 1;
  }
  .contact li { margin-bottom: 12px; }
  .contact .contact-phone { margin-top: 22px; }
</style>
</head>
<body>
<main class="canvas">

  <section class="card-front" aria-label="Business card front">
    <div class="quilt-area quilt-area--top" role="img" aria-label="Black tufted leather pattern with gold diamond lines and fleur ornaments"></div>
    <div class="name-band">
      <span class="brand-name">NowQuillo</span>
    </div>
    <div class="quilt-area quilt-area--bottom" role="img" aria-label="Black tufted leather pattern with gold diamond lines and fleur ornaments"></div>
  </section>

  <section class="card-back" aria-label="Business card back">
    <span class="brand-name brand-name--vertical">NowQuillo</span>
    <svg class="divider" viewBox="0 0 2 272" preserveAspectRatio="none" aria-hidden="true">
      <defs>
        <linearGradient id="divider-fade" x1="0" y1="0" x2="0" y2="1">
          <stop offset="0" stop-color="#c9962a" stop-opacity="0"/>
          <stop offset="0.2" stop-color="#c9962a"/>
          <stop offset="0.8" stop-color="#c9962a"/>
          <stop offset="1" stop-color="#c9962a" stop-opacity="0"/>
        </linearGradient>
      </defs>
      <rect width="2" height="272" fill="url(#divider-fade)"/>
    </svg>
    <ul class="contact">
      <li class="contact-name">Name</li>
      <li class="contact-web">www.nowquillo-example.com</li>
      <li class="contact-phone">555-013-7720</li>
    </ul>
  </section>

</main>
</body>
</html>
```